Wayline Billboard Co Business Card Design

We have a newly created business and logo, but we now need business cards using the new logo.
We are an Australian based business, and we sell advertising space on trucks. The business cards will be seen by media buyers, direct advertisers, fleet owners and business people in general.
Our colours are very simple - black and a strong yellow, with some white. We have chosen the black and yellow for various reasons, but in particular because they are high contrast, and they also have a parallel with the number plates used on our roads, which is relevant to our product offering.
My initial thoughts:
Keep it simple and uncluttered
Use both sides
Our default is Century Gothic
I can provide logo files as required. We do not yet have a website, so I can't direct you there just yet. That may well be another project!
Target Market(s)
The business cards will be seen by media buyers, direct advertisers, fleet owners and business people in general.
Industry/Entity Type
Advertising
Look and feel
Each slider illustrates characteristics of the customer's brand and the style your logo design should communicate.

```html
<!DOCTYPE html>
<html lang="en">
<head>
<meta charset="utf-8">
<title>Wayline Billboard Co – Business Card</title>
<link rel="stylesheet" href="https://fonts.googleapis.com/css2?family=Didact+Gothic&display=swap">
<style>
  :root {
    --backdrop: #5e5e5e;
    --card-black: #0b0b0b;
    --card-white: #f7f7f7;
    --brand-yellow: #f2df0c;
    --ink: #1a1a1a;
    --rule: #222222;
  }
  * { box-sizing: border-box; margin: 0; padding: 0; }
  html, body {
    width: 1200px; height: 900px; overflow: hidden;
    background: var(--backdrop);
    font-family: "Didact Gothic", "Century Gothic", sans-serif;
  }
  .stage {
    width: 1200px; height: 900px;
    display: flex; flex-direction: column; align-items: center; justify-content: center;
    gap: 40px;
  }
  .card {
    width: 640px; height: 391px; position: relative;
    box-shadow: 0 10px 24px rgba(0,0,0,.35);
  }
  /* Front: black side */
  .card--front {
    background: var(--card-black);
    display: flex; flex-direction: column; align-items: center; justify-content: center;
  }
  .brand-lockup {
    display: flex; align-items: center; gap: 14px;
    color: var(--brand-yellow); font-size: 34px; letter-spacing: 2px;
    text-transform: uppercase;
  }
  .brand-lockup__square { width: 22px; height: 22px; background: var(--brand-yellow); }
  .card__website {
    position: absolute; bottom: 52px; left: 0; right: 0; text-align: center;
    color: var(--brand-yellow); font-size: 17px; letter-spacing: .5px;
  }
  /* Back: white side */
  .card--back { background: var(--card-white); color: var(--ink); }
  .back-brand {
    position: absolute; top: 58px; right: 40px;
    display: flex; align-items: center; gap: 10px;
    font-size: 21px; letter-spacing: 1px; text-transform: uppercase; color: var(--ink);
  }
  .back-brand__square { width: 16px; height: 16px; background: var(--brand-yellow); }
  .person { position: absolute; left: 40px; top: 140px; }
  .person__name { font-size: 26px; letter-spacing: 1px; text-transform: uppercase; font-weight: 400; }
  .person__role { font-size: 17px; margin-top: 4px; }
  .divider {
    position: absolute; left: 40px; right: 40px; top: 222px;
    border-top: 1.5px solid var(--rule);
  }
  .contact-list { position: absolute; left: 40px; top: 242px; list-style: none; }
  .contact-list li {
    display: flex; align-items: center; gap: 10px;
    font-size: 16px; line-height: 22px;
  }
  .contact-list svg { width: 13px; height: 13px; flex: none; }
  .postal {
    position: absolute; left: 400px; top: 264px;
    font-style: normal; font-size: 17px; line-height: 23px;
  }
</style>
</head>
<body>
<main class="stage">
  <section class="card card--front" aria-label="Card front">
    <div class="brand-lockup">
      <span class="brand-lockup__square"></span>
      <span>Wayline Billboard Co</span>
    </div>
    <p class="card__website">wayline-ads.com.au</p>
  </section>

  <section class="card card--back" aria-label="Card back">
    <div class="back-brand">
      <span class="back-brand__square"></span>
      <span>Wayline Billboard Co</span>
    </div>
    <div class="person">
      <h1 class="person__name">Dale Harper</h1>
      <p class="person__role">Founder</p>
    </div>
    <hr class="divider">
    <ul class="contact-list">
      <li>
        <svg viewBox="0 0 16 16" aria-hidden="true"><path fill="#f2df0c" d="M3 1l3 3-1.5 2a9 9 0 0 0 5.5 5.5L12 10l3 3-2 2C7 15 1 9 1 3z"/></svg>
        <span>1800WAYLINE</span>
      </li>
      <li>
        <svg viewBox="0 0 16 16" aria-hidden="true"><rect x="4" y="1" width="8" height="14" rx="1.5" fill="#f2df0c"/><rect x="5.5" y="3" width="5" height="8" fill="#f7f7f7"/></svg>
        <span>+61 4 0000 5512</span>
      </li>
      <li>
        <svg viewBox="0 0 16 16" aria-hidden="true"><rect x="1" y="3" width="14" height="10" fill="#f2df0c"/><path d="M1 3l7 6 7-6" fill="none" stroke="#f7f7f7" stroke-width="1.4"/></svg>
        <span>dale@wayline-ads.com.au</span>
      </li>
    </ul>
    <address class="postal">
      Wayline Billboard Co<br>
      PO Box 4471<br>
      Harbour Flat NSW 2099
    </address>
  </section>
</main>
</body>
</html>
```